Wedding Invitation Design Project

We are wanting 2 wedding invitation designs that would consist of:

1. Floral Design
2. Beach Theme Design

The size of the invitations can be any of the following sizes:

105 x 148mm
100 x 210mm
150 x 150mm

The invitations will be commercially printed digitally.

We are open to any ideas that you may have but would like the cards to be a little different to the norm i.e not just have a picture of a sandy beach for the beach theme invite but saying that it will still need the invites to have a wider appeal.

The winner of this project will also need to provide matching cards that are:

1. Save this date Card
2. Seating Card
3. Table number Card
4. Thank you Card

Industry/Entity Type

Wedding

```html
<!DOCTYPE html>
<html lang="en">
<head>
<meta charset="utf-8">
<title>Wedding Invitation – Floral</title>
<link rel="stylesheet" href="https://fonts.googleapis.com/css2?family=Pinyon+Script&family=Noto+Serif&display=swap">
<style>
  :root {
    --paper: #ffffff;
    --backdrop: #d9d9d9;
    --magenta: #b81c66;
    --magenta-soft: #c94a86;
    --ink: #2b2b2b;
    --rule: #777777;
    --script-pink: #b53a79;
  }
  html, body {
    margin: 0;
    padding: 0;
    width: 910px;
    height: 1200px;
    overflow: hidden;
    background: var(--backdrop);
  }
  .invitation {
    position: relative;
    width: 910px;
    height: 1200px;
    background: var(--paper);
    overflow: hidden;
    font-family: "Noto Serif", Georgia, serif;
    color: var(--ink);
  }
  .floral-border {
    position: absolute;
    inset: 0;
    width: 910px;
    height: 1200px;
  }
  .text {
    position: absolute;
    margin: 0;
    line-height: 1;
    white-space: nowrap;
  }
  .greeting {
    left: 61px;
    top: 212px;
    font-family: "Pinyon Script", cursive;
    font-size: 56px;
    color: var(--ink);
  }
  .fill-line {
    position: absolute;
    height: 0;
    border-top: 1px solid var(--rule);
  }
  .greeting-line { left: 193px; top: 270px; width: 480px; }
  .hosts-line { left: 224px; top: 387px; width: 491px; }
  .body-copy { font-size: 25px; }
  .hosts { left: 63px; top: 358px; }
  .request { left: 63px; top: 422px; line-height: 32px; }
  .couple-name {
    font-family: "Pinyon Script", cursive;
    font-size: 82px;
    color: var(--script-pink);
  }
  .couple-name .dots {
    font-family: "Noto Serif", Georgia, serif;
    font-size: 24px;
    letter-spacing: 1px;
  }
  .partner-a { left: 232px; top: 520px; }
  .conjunction {
    left: 356px;
    top: 608px;
    font-family: "Pinyon Script", cursive;
    font-size: 46px;
    color: var(--script-pink);
  }
  .partner-b { left: 232px; top: 668px; }
  .date { left: 63px; top: 802px; line-height: 32px; }
  .rsvp { left: 63px; top: 955px; }
</style>
</head>
<body>
<main class="invitation">
  <svg class="floral-border" viewBox="0 0 910 1200" role="img" aria-label="Magenta corner border with swirling vines and pink lily flowers along the right and bottom edges">
    <defs>
      <linearGradient id="border-tone" x1="0" y1="0" x2="0.4" y2="1">
        <stop offset="0" stop-color="var(--magenta)"/>
        <stop offset="0.5" stop-color="var(--magenta-soft)"/>
        <stop offset="1" stop-color="var(--magenta)"/>
      </linearGradient>
    </defs>
    <path fill="url(#border-tone)" d="M451 0 C480 40 500 60 520 70 C580 110 620 170 667 200 C710 230 750 245 773 270 C805 305 820 340 815 370 C808 430 800 500 804 550 C808 620 790 670 773 710 C758 750 760 800 751 830 C740 890 720 930 688 960 C660 1000 640 1040 604 1060 C560 1090 510 1100 456 1110 C400 1118 350 1110 298 1120 C240 1130 190 1145 140 1160 C90 1175 40 1190 3 1200 L910 1200 L910 0 Z"/>
  </svg>

  <p class="text greeting">Dear</p>
  <div class="fill-line greeting-line"></div>

  <p class="text body-copy hosts">Mr and Mrs</p>
  <div class="fill-line hosts-line"></div>

  <p class="text body-copy request">request the honour of your presense<br>at the marriage of</p>

  <p class="text couple-name partner-a">A<span class="dots">................</span></p>
  <p class="text conjunction">and</p>
  <p class="text couple-name partner-b">B<span class="dots">..............</span></p>

  <p class="text body-copy date">SATURDAY, OCTOBER 12, 2013<br>at ............. Church, ......................</p>

  <p class="text body-copy rsvp">Please email RSVP to ...........@inboxmail.net</p>
</main>
</body>
</html>
```